Business Card Design Project

The business card is for an educational company that provides personalised tuition to students.

The company logo is in orange and blue (as provided) and should be included in the name card design

The philosophy of the company is to make learning a comfortable experience for student as such design of the namecard should look fresh and has a bit of the 'wow' factor. Some of the namecard design that appeals to me are as uploaded under Sample Design.

The particulars that need to be provided are:
(1): Company Name (Quillmark Education)
(1): Name
(2): Educational qualifications which will appear below name
(3): Mobile number
(4): Email address
(5): Website

Industry/Entity Type

Business

Requirements
Must have
• (1): Company Logo

(2): The card background should preferably be coloured both for the front side and back.

(3): The choice of font is important as part of the selection consideration. There is no preferred font that I have selected, designer is free to choose the font that will complement their design.

```html
<!DOCTYPE html>
<html lang="en">
<head>
<meta charset="utf-8">
<title>Quillmark Education Business Cards Samples</title>
<link rel="stylesheet" href="https://fonts.googleapis.com/css2?family=Roboto+Condensed:wght@400;700&display=swap">
<style>
  :root {
    --paper: #ffffff;
    --card-yellow: #fff200;
    --brand-orange: #f15a29;
    --brand-blue: #29a9e0;
    --ink: #231f20;
  }
  * { margin: 0; padding: 0; box-sizing: border-box; }
  html, body {
    width: 900px;
    height: 1200px;
    overflow: hidden;
    background: var(--paper);
    font-family: "Roboto Condensed", "Arial Narrow", Arial, sans-serif;
    color: var(--ink);
  }
  .sheet { position: relative; width: 900px; height: 1200px; }
  .sheet-title {
    position: absolute; top: 7px; left: 0; width: 900px;
    text-align: center; font-size: 17px; font-weight: 400;
  }
  .card {
    position: absolute; width: 401px; height: 258px;
    background: var(--card-yellow); overflow: hidden;
  }
  .card--front { left: 0; }
  .card--back { left: 439px; }
  .row-1 { top: 138px; }
  .row-2 { top: 542px; }
  .row-3 { top: 941px; height: 259px; }

  .stripe { position: absolute; top: 0; height: 100%; }
  .card--front .stripe--blue { left: 346px; width: 12px; background: var(--brand-blue); }
  .card--front .stripe--orange { left: 358px; width: 43px; background: var(--brand-orange); }
  .card--back .stripe--orange { left: 0; width: 42px; background: var(--brand-orange); }
  .card--back .stripe--blue { left: 42px; width: 12px; background: var(--brand-blue); }

  .brand-mark {
    position: absolute; left: 18px; top: 66px;
    width: 130px; height: 129px;
    background: var(--brand-orange); border-radius: 16px;
  }
  .brand-name {
    position: absolute; left: 154px; top: 82px;
    font-size: 38px; line-height: 38px; font-weight: 700;
    color: var(--ink);
  }

  .ribbon { position: absolute; left: 346px; width: 55px; height: 48px; }
  .ribbon-tab { position: absolute; left: 0; width: 54px; height: 48px; background: var(--ink); }
  .row-2 .ribbon, .row-2 .ribbon-tab { top: 110px; }
  .row-3 .ribbon, .row-3 .ribbon-tab { top: 45px; }

  .company-line {
    position: absolute; left: 66px; top: 12px;
    font-size: 18px; line-height: 24px;
  }
  .row-3 .company-line { left: 10px; top: 18px; }
  .contact-list {
    position: absolute; left: 66px; top: 90px;
    list-style: none; font-size: 18px; line-height: 24px;
  }
  .row-3 .contact-list { left: 12px; top: 157px; }

  .sample-number {
    position: absolute; left: 874px; font-size: 17px;
  }
</style>
</head>
<body>
<main class="sheet">
  <h1 class="sheet-title">Quillmark Education Business Cards Samples</h1>

  <!-- Sample 1 -->
  <section class="card card--front row-1">
    <div class="brand-mark"></div>
    <div class="brand-name">Quillmark<br>Education</div>
    <div class="stripe stripe--blue"></div>
    <div class="stripe stripe--orange"></div>
  </section>
  <section class="card card--back row-1">
    <div class="stripe stripe--orange"></div>
    <div class="stripe stripe--blue"></div>
    <p class="company-line">Quillmark Education</p>
    <ul class="contact-list">
      <li>Name:</li><li>Mobile number:</li><li>Email address:</li><li>Website:</li>
    </ul>
  </section>
  <span class="sample-number" style="top:240px">1</span>

  <!-- Sample 2 -->
  <section class="card card--front row-2">
    <div class="brand-mark"></div>
    <div class="brand-name">Quillmark<br>Education</div>
    <div class="stripe stripe--blue"></div>
    <div class="stripe stripe--orange"></div>
    <svg class="ribbon" viewBox="0 0 55 48" aria-hidden="true">
      <polygon points="0,0 55,0 55,48 0,48 15,24" fill="#231f20"/>
    </svg>
  </section>
  <section class="card card--back row-2">
    <div class="stripe stripe--orange"></div>
    <div class="stripe stripe--blue"></div>
    <div class="ribbon-tab"></div>
    <p class="company-line">Quillmark Education</p>
    <ul class="contact-list">
      <li>Name:</li><li>Mobile number:</li><li>Email address:</li><li>Website:</li>
    </ul>
  </section>
  <span class="sample-number" style="top:665px">2</span>

  <!-- Sample 3 -->
  <section class="card card--front row-3">
    <div class="brand-mark"></div>
    <div class="brand-name">Quillmark<br>Education</div>
    <svg class="ribbon" viewBox="0 0 55 48" aria-hidden="true">
      <polygon points="0,0 55,0 55,48 0,48 15,24" fill="#231f20"/>
    </svg>
  </section>
  <section class="card card--back row-3">
    <div class="ribbon-tab" style="left:0"></div>
    <p class="company-line">Quillmark Education</p>
    <ul class="contact-list">
      <li>Name:</li><li>Mobile number:</li><li>Email address:</li><li>Website:</li>
    </ul>
  </section>
  <span class="sample-number" style="top:1057px">3</span>
</main>
</body>
</html>
```